依頼詳細
・デザイン概要
今回は、トップページデザインの募集になります。
レスポンシブデザインのサイトで、bootstrap4を利用しコーディングする予定になります。
デザイン幅は2000px、コンテンツの幅はbootstrap4デフォルトの1110pxを基準としてください。ただし最近のデザインの流行を取りいれて、フルワイドや、1200~15000px程度の幅のコンテンツをバランスよくレイアウトしてください。
コンテンツ配置は基本12分割になります。がデザインによっては、多少逸脱してもかまいません。
(12分割のコンテンツ幅については添付のPSDを参考にご覧ください)

本文のフォントはゴシック系は游ゴシック、メイリオ、明朝系は遊明朝でお願いします。
飾り文字はフリーフォントか、googleフォントを利用してください。

メイン画像部分・グローバルメニューは、ワイド適用でお願いします。

掲載画像については、基本は添付ファイルを使用してください。
また、雰囲気が合っていれば、指定外の画像を追加掲載いただいてOKです。

・その他
デザイン・ムード、参考サイトについてなど、掲載内容詳細に関しては、別添のExcel資料を参照してください。

資料上はサイト名(社名)や住所などは伏字にしております。ご提案時点ではそのまま作成をお願いします。当選確定後、本内容に修正をお願いいたします。

当選の方は、希望があれば引き続き下層ページの作成及びコーディング作業を依頼可能です。
ページ数
1ページ
希望イメージ
シンプル 複雑
単色 カラフル
暗い 明るい
日常 高級
遊び心 厳粛
未来的 伝統的
女性的 男性的
希望する色
青系
納品ファイル
• 高解像度JPG (.jpg)
• フォトショップ形式 (.psd)

クライアントと折衝しまして、norvikaplane様のデザインが一番「落ち着いてる雰囲気」と「町工場な印象」を感じたとのことで、当選とさせていただきました。

本件、多数のご提案ありがとうございました。
どの提案もとてもよく、クライアントもかなり悩んでいましたがら、最終的にムードや印象の部分でnorvikaplane様を当選とさせていいただきました。
どうもありがとうございました。
今後とも宜しくお願いいたします。

```html
<!DOCTYPE html>
<html lang="ja">
<head>
<meta charset="utf-8">
<title>有限会社〇〇〇〇製作所</title>
<link rel="stylesheet" href="https://fonts.googleapis.com/css2?family=Noto+Serif+JP:wght@400;600;700&family=Noto+Sans+JP:wght@400;500&family=Cormorant+Garamond:wght@400;500&display=swap">
<style>
:root{
  --navy:#1d3f7c;
  --navy-deep:#13264d;
  --ink:#222;
  --white:#fff;
  --charcoal:#2c2c2c;
  --grey-text:#d8d8d8;
  --muted:#666;
}
*{margin:0;padding:0;box-sizing:border-box}
html,body{width:745px;height:1200px;overflow:hidden}
body{position:relative;background:var(--white);font-family:"Noto Sans JP",sans-serif;color:var(--ink)}
.abs{position:absolute}

/* hero */
.hero{left:0;top:0;width:745px;height:236px}
.hero-photo{position:absolute;inset:0;background:linear-gradient(180deg,#8b8e92 0%,#a7a9ab 35%,#6f7276 70%,#4a4c50 100%)}
.hero-shade{position:absolute;inset:0;background:linear-gradient(180deg,rgba(0,0,0,.15),rgba(0,0,0,.05) 40%,rgba(0,0,0,.35))}
.site-header{position:absolute;left:0;top:0;width:745px;height:48px;display:flex;align-items:center;padding-left:228px;gap:20px}
.brand{font-family:"Noto Serif JP",serif;font-size:11px;font-weight:600;color:var(--white);margin-right:14px}
.gnav{display:flex;gap:18px;list-style:none}
.gnav li{font-size:8px;color:var(--white)}
.hero-copy{position:absolute;left:0;top:92px;width:745px;text-align:center;color:var(--white)}
.hero-title{font-family:"Noto Serif JP",serif;font-weight:700;font-size:24px;letter-spacing:2px;text-shadow:0 1px 4px rgba(0,0,0,.5)}
.hero-sub{font-family:"Cormorant Garamond",serif;font-size:10px;margin-top:4px;letter-spacing:1px}

/* intro */
.intro{left:0;top:236px;width:745px;height:139px;background:var(--charcoal);overflow:hidden}
.intro-deco{position:absolute;left:0;top:12px;width:745px;text-align:center;font-family:"Cormorant Garamond",serif;font-size:50px;color:rgba(255,255,255,.1);letter-spacing:2px;line-height:60px}
.intro-text{position:absolute;left:0;top:22px;width:745px;text-align:center;font-size:7px;line-height:1.9;color:var(--grey-text)}

/* blue features */
.features{left:0;top:375px;width:745px;height:606px;background:var(--navy)}
.card{position:absolute;background:var(--white);padding:26px 24px}
.card-title{display:flex;align-items:center;gap:10px;font-family:"Noto Serif JP",serif;font-size:20px;font-weight:700;color:var(--ink)}
.card-title::before{content:"";width:28px;height:2px;background:var(--ink)}
.card-lead{font-family:"Noto Serif JP",serif;font-size:10px;color:var(--navy);margin:8px 0 16px 38px}
.card-body{font-size:6.5px;line-height:1.8;color:var(--muted)}
.btn-more{display:inline-block;margin-top:18px;background:var(--navy);color:var(--white);font-size:6px;letter-spacing:1px;width:64px;height:14px;line-height:14px;padding-left:10px}
.photo{position:absolute}
.tech-card{left:161px;top:36px;width:300px;height:240px}
.tech-photo{left:373px;top:35px;width:212px;height:186px;background:linear-gradient(135deg,#cfd2d5,#7c8086 55%,#3c3f44)}
.product-photo{left:161px;top:333px;width:236px;height:174px;background:linear-gradient(135deg,#e0e2e4,#9a9ea3 50%,#55595e)}
.product-card{left:373px;top:370px;width:212px;height:187px;padding:22px 18px}
.product-card .card-title{font-size:18px}

/* company */
.company{left:0;top:981px;width:745px;height:149px}
.company-photo{position:absolute;left:0;top:0;width:373px;height:149px;background:linear-gradient(180deg,#55585c,#1f2124)}
.company-copy{position:absolute;left:150px;top:18px;color:var(--white)}
.company-copy .card-title{color:var(--white);font-size:20px}
.company-copy .card-title::before{background:var(--white)}
.company-copy p{font-size:6.5px;line-height:1.8;margin-top:12px;color:#e6e6e6}
.company-map{position:absolute;left:373px;top:0;width:372px;height:149px;background:linear-gradient(135deg,#eceee8,#dde3ea)}

/* footer */
.site-footer{left:0;top:1130px;width:745px;height:70px;background:var(--navy-deep);color:var(--white);padding:12px 0 0 161px}
.footer-brand{font-family:"Noto Serif JP",serif;font-size:11px;font-weight:600}
.footer-brand small{font-family:"Noto Sans JP",sans-serif;font-size:6px;font-weight:400;margin-left:14px;opacity:.8}
.footer-info{font-size:6px;line-height:1.7;margin-top:5px;opacity:.85}
</style>
</head>
<body>

<section class="hero abs">
  <div class="hero-photo" role="img" aria-label="ばね製造工場の作業場の写真"></div>
  <div class="hero-shade"></div>
  <header class="site-header">
    <span class="brand">有限会社〇〇〇〇製作所</span>
    <ul class="gnav">
      <li>ホーム</li><li>技術紹介</li><li>製品紹介</li><li>会社案内</li><li>お問合せ</li>
    </ul>
  </header>
  <div class="hero-copy">
    <h1 class="hero-title">圧倒的クオリティでバネを作り上げる</h1>
    <p class="hero-sub">Create springs with overwhelming quality</p>
  </div>
</section>

<section class="intro abs">
  <div class="intro-deco" aria-hidden="true">Excellent Works</div>
  <p class="intro-text">〇〇〇〇製作所は、創業以来精密ばねの製造一筋に歩んでまいりました。<br>熟練の職人による確かな技術と最新設備により、お客様のご要望に応える<br>高品質な製品をお届けします。小ロットから量産まで幅広く対応いたします。</p>
</section>

<section class="features abs">
  <div class="photo tech-photo" role="img" aria-label="ばね加工機械の写真"></div>
  <article class="card tech-card">
    <h2 class="card-title">技術紹介</h2>
    <p class="card-lead">解析の設計と高い技術力</p>
    <p class="card-body">長年培った経験と確かな技術で、<br>お客様の多様なご要望にお応えする製品を作ります。<br>設計から加工まで一貫対応いたします。</p>
    <span class="btn-more">MORE</span>
  </article>

  <div class="photo product-photo" role="img" aria-label="金属製ばね製品の写真"></div>
  <article class="card product-card">
    <h2 class="card-title">製品紹介</h2>
    <p class="card-lead">高精度・高品質な製品加工</p>
    <p class="card-body">圧縮ばね・引張ばね・ねじりばねなど、<br>用途に合わせた様々な製品を製造しています。<br>詳しくは製品一覧をご覧ください。</p>
    <span class="btn-more">MORE</span>
  </article>
</section>

<section class="company abs">
  <div class="company-photo" role="img" aria-label="巻かれた線材コイルの写真"></div>
  <div class="company-copy">
    <h2 class="card-title">会社案内</h2>
    <p>会社概要・沿革・アクセスなど、<br>当社についてご紹介いたします。</p>
  </div>
  <div class="company-map" role="img" aria-label="所在地周辺の地図"></div>
</section>

<footer class="site-footer abs">
  <div class="footer-brand">有限会社〇〇〇〇製作所<small>TEL 000-000-0000</small></div>
  <p class="footer-info">〒000-0000 〇〇県〇〇市〇〇町0-0<br>営業時間 8:30〜17:30（土日祝休）</p>
</footer>

</body>
</html>
```